Woman owned consulting company needs an elegant and modern business card design

I need a business card design for my new consulting company, Mira Holcombe Consulting. I am looking for something that is simple and elegant, but also creative and original. You can use either version of the logo that are attached. I have also included the information that needs to be featured on the business card.

Contact Information for Business Card

Requirements
Must have
• The logo and the font type and a standard business card size. Use shades of gray/silver and or rose gold that are in the logo.
• I didn't realize that my actual logo wasn't attached. Please incorporate in the designs.
Should not have
• Colors that are different from my logo

```html
<!DOCTYPE html>
<html lang="en">
<head>
<meta charset="utf-8">
<title>Mira Holcombe Consulting – Business Card</title>
<link rel="stylesheet" href="https://fonts.googleapis.com/css2?family=Roboto:wght@300;400;500&display=swap">
<style>
  :root {
    --backdrop: #262626;
    --brand-red: #c5222b;
    --card-red: #c4222a;
    --rose-tint: #e3b4b8;
    --card-white: #e2e2e2;
    --card-white-light: #ebebeb;
    --text-gray: #6f6f6f;
    --name-gray: #6a6a6a;
    --deco-gray: #acacac;
  }
  * { margin: 0; padding: 0; box-sizing: border-box; }
  html, body {
    width: 1200px;
    height: 764px;
    overflow: hidden;
    background: var(--backdrop);
    font-family: "Roboto", Arial, sans-serif;
  }
  .stage {
    position: relative;
    width: 1200px;
    height: 764px;
  }
  .card {
    position: absolute;
    width: 437px;
    height: 250px;
    box-shadow: 0 8px 22px rgba(0, 0, 0, 0.55);
  }

  /* Front */
  .card--front {
    left: 133px;
    top: 249px;
    background: var(--card-red);
    display: flex;
    align-items: center;
    justify-content: center;
  }
  .brand-name {
    color: var(--rose-tint);
    font-weight: 300;
    font-size: 24px;
    letter-spacing: 0.5px;
  }

  /* Back */
  .card--back {
    left: 630px;
    top: 248px;
    background: linear-gradient(100deg, var(--card-white-light) 0%, var(--card-white) 100%);
  }
  .brand-mark-faint {
    position: absolute;
    left: 26px;
    top: 22px;
    width: 80px;
    color: var(--deco-gray);
    font-weight: 300;
    font-size: 13px;
    line-height: 1.35;
  }
  .contact {
    position: absolute;
    right: 28px;
    top: 20px;
    color: var(--text-gray);
  }
  .contact__name {
    font-weight: 400;
    font-size: 34px;
    line-height: 1.1;
    color: var(--name-gray);
    margin-bottom: 6px;
  }
  .contact__surname { color: var(--brand-red); }
  .contact__role {
    font-size: 11.5px;
    line-height: 1.3;
    margin-bottom: 3px;
  }
  .contact__title {
    color: var(--brand-red);
    font-weight: 500;
  }
  .contact__line {
    font-size: 13.5px;
    line-height: 17px;
    letter-spacing: 0.2px;
  }
  .website {
    position: absolute;
    left: 131px;
    top: 208px;
    font-size: 12.5px;
    color: var(--text-gray);
    letter-spacing: 0.2px;
  }
</style>
</head>
<body>
  <main class="stage">
    <section class="card card--front" aria-label="Business card front">
      <span class="brand-name">Mira Holcombe Consulting</span>
    </section>

    <section class="card card--back" aria-label="Business card back">
      <div class="brand-mark-faint">Mira Holcombe Consulting</div>

      <div class="contact">
        <h1 class="contact__name">Mira <span class="contact__surname">Holcombe</span></h1>
        <p class="contact__role"><span class="contact__title">CEO,</span> Mira Holcombe Consulting, LLC</p>
        <p class="contact__line">mira@miraholcombeconsulting.com</p>
        <p class="contact__line">610-555-0142</p>
      </div>

      <p class="website">www.miraholcombeconsulting.com</p>
    </section>
  </main>
</body>
</html>
```